Mossy Den Pet Supply

Thank you for your interest in this design contest. We are always welcome to questions and are looking forward to seeing what you can come up with.

We work on a Bootstrap platform with our custom built CMS. We require all designs to be sized accordingly with the bootstrap grid system found here: http://fernlattice.com/css/#grid

At the start of a competition, we are looking for general Home Page Design concepts and an example product grid page.

Homepage: Slide Show/Featured Products/Specials

example website as a reference:https://www.mintcollarworks.com/

Store Product Grid: Show a grid of product thumbnails. Included elements are thumbnail and price. Also included are filters (sort by, show by grid/list).

No photos at this time but Logo is attached. Looking for good quality photo's around the web. Please read the attached creative brief in depth to get an idea f what the client is looking for. Thanks!

```html
<!DOCTYPE html>
<html lang="en">
<head>
<meta charset="utf-8">
<title>Mossy Den Pet Supply</title>
<link href="https://fonts.googleapis.com/css2?family=Open+Sans:wght@400;600;700&display=swap" rel="stylesheet">
<style>
:root{
  --green:#8cc63f;
  --green-dark:#6e9e1f;
  --green-active:#5f8f1c;
  --footer:#6c9a1f;
  --footer-bottom:#2f2f2f;
  --ink:#333;
  --muted:#777;
  --btn:#2b2b2b;
  --white:#fff;
}
*{box-sizing:border-box;margin:0;padding:0}
html,body{width:1200px;height:2164px;overflow:hidden}
body{font-family:"Open Sans",Arial,sans-serif;color:var(--ink);background:var(--white);position:relative}
.topline{position:absolute;left:0;top:0;width:1200px;height:7px;background:var(--green)}
.brand{position:absolute;left:89px;top:14px;width:147px;height:150px;display:flex;flex-direction:column;align-items:center;justify-content:center;gap:10px;text-align:center}
.brand-mark{width:34px;height:34px;background:var(--ink)}
.brand-name{font-weight:700;font-size:21px;line-height:24px;color:var(--ink)}
.search{position:absolute;left:349px;top:43px;width:327px;height:46px;border:3px solid #c9c9c9;background:#fff;display:flex;align-items:center;padding:0 12px;font-size:17px;color:#999}
.search svg{position:absolute;right:10px;top:9px}
.account{position:absolute;top:0;right:88px;display:flex;gap:7px}
.account a{background:var(--green);color:#fff;font-size:15px;height:38px;display:flex;align-items:center;gap:8px;padding:0 14px;text-decoration:none}
.origin{position:absolute;left:729px;top:62px;font-size:13px;font-weight:700;color:#555;letter-spacing:.3px}
.flag{position:absolute;left:885px;top:57px;width:34px;height:32px;background:linear-gradient(#b22234 0 14%,#fff 14% 28%,#b22234 28% 42%,#fff 42% 57%,#b22234 57% 71%,#fff 71% 85%,#b22234 85%)}
.social{position:absolute;left:928px;top:57px;display:flex;gap:6px}
.social span{width:32px;height:32px;display:block}
.nav{position:absolute;left:236px;top:115px;width:964px;height:53px;background:var(--green);display:flex;align-items:stretch;padding-left:94px}
.nav a{color:#fff;text-decoration:none;font-weight:700;font-size:16px;display:flex;align-items:center;padding:0 16px}
.nav a.active{background:var(--green-active);flex-direction:column;justify-content:center;gap:2px;padding:0 18px}
.hero{position:absolute;left:0;top:168px;width:1200px;height:549px;background:linear-gradient(100deg,#6b4a35 0%,#a98466 30%,#c7b3a8 45%,#8c2234 60%,#9b7a5a 80%,#e8e6e0 100%)}
.hero-caption{position:absolute;left:173px;top:396px}
.hero-title{display:inline-block;background:rgba(0,0,0,.55);color:#fff;font-weight:600;font-size:48px;line-height:66px;padding:0 10px}
.hero-sub{display:inline-block;margin-top:10px;background:rgba(0,0,0,.55);color:#fff;font-size:26px;line-height:40px;padding:0 10px}
.hero-arrow{position:absolute;top:428px;width:36px;height:36px;border-radius:50%;background:rgba(255,255,255,.85)}
.dots{position:absolute;top:689px;left:563px;display:flex;gap:10px}
.dots span{width:15px;height:15px;border-radius:50%;background:#bbb}
.dots span.on{background:#fff}
.products{position:absolute;left:89px;top:825px;width:1022px;display:grid;grid-template-columns:repeat(3,326px);column-gap:22px;row-gap:74px}
.product{text-align:center}
.product-photo{height:229px}
.product-title{margin-top:24px;font-size:20px;line-height:25px;color:var(--ink)}
.product-price{margin-top:12px;font-size:27px;font-weight:700;color:var(--green)}
.add-cart{margin:8px auto 0;width:118px;height:43px;background:var(--btn);color:#fff;font-size:15px;font-weight:700;display:flex;align-items:center;justify-content:center}
.footer{position:absolute;left:0;top:1792px;width:1200px;height:312px;background:var(--footer);color:#fff}
.footer-col{position:absolute;top:26px}
.footer-col h3{font-weight:400;font-size:25px;margin-bottom:14px}
.footer-col li{list-style:none;font-size:16px;line-height:26px;color:#e6f2cf}
.news p{font-size:16px;line-height:23px;color:#e6f2cf;width:340px}
.news time{display:block;font-size:12px;color:#c9dcaa;font-style:italic;margin:8px 0 24px}
.copyright{position:absolute;left:0;top:2104px;width:1200px;height:60px;background:var(--footer-bottom);color:#fff;font-size:15px;display:flex;align-items:center;padding-left:89px}
</style>
</head>
<body>
<div class="topline"></div>

<div class="brand"><span class="brand-mark"></span><span class="brand-name">Mossy Den<br>Pet Supply</span></div>

<div class="search">Search here
  <svg width="26" height="26" viewBox="0 0 26 26"><circle cx="11" cy="11" r="7.5" fill="none" stroke="#aaa" stroke-width="3"/><line x1="16.5" y1="16.5" x2="23" y2="23" stroke="#aaa" stroke-width="3.5"/></svg>
</div>

<div class="account">
  <a href="#"><svg width="16" height="16" viewBox="0 0 16 16"><circle cx="8" cy="5" r="4" fill="#fff"/><path d="M1 16c0-4 3-6 7-6s7 2 7 6z" fill="#fff"/></svg>Login</a>
  <a href="#"><svg width="20" height="16" viewBox="0 0 20 16"><path d="M0 5h20l-3 9H3z" fill="#fff"/><path d="M5 5l5-5 5 5" fill="none" stroke="#fff" stroke-width="2"/></svg><b>0</b> item(s)</a>
</div>

<div class="origin">HANDCRAFTED IN USA</div>
<div class="flag" role="img" aria-label="Striped national flag"></div>
<div class="social">
  <span style="background:#f2a900"></span>
  <span style="background:#3b5998"></span>
  <span style="background:#1da1f2"></span>
  <span style="background:#dd4b39"></span>
  <span style="background:#0e76a8"></span>
</div>

<nav class="nav">
  <a href="#" class="active"><svg width="14" height="12" viewBox="0 0 14 12"><circle cx="3" cy="3" r="2" fill="#fff"/><circle cx="7" cy="1.8" r="1.8" fill="#fff"/><circle cx="11" cy="3" r="2" fill="#fff"/><ellipse cx="7" cy="8.5" rx="4" ry="3.2" fill="#fff"/></svg>Home</a>
  <a href="#">Blog</a><a href="#">E-commerce</a><a href="#">Reservations</a><a href="#">Event Calendar</a><a href="#">Photos</a><a href="#">Videos</a><a href="#">News</a>
</nav>

<section class="hero" role="img" aria-label="Brown puppy sitting in a plush red pet bed by a window"></section>
<div class="hero-caption">
  <div class="hero-title">We Speak his language</div><br>
  <div class="hero-sub">From woof to whine and everything in between.</div>
</div>
<div class="hero-arrow" style="left:94px"><svg width="36" height="36" viewBox="0 0 36 36"><path d="M21 11l-7 7 7 7" fill="none" stroke="#555" stroke-width="3"/></svg></div>
<div class="hero-arrow" style="left:1070px"><svg width="36" height="36" viewBox="0 0 36 36"><path d="M15 11l7 7-7 7" fill="none" stroke="#555" stroke-width="3"/></svg></div>
<div class="dots"><span class="on"></span><span></span><span></span></div>

<section class="products">
  <div class="product"><div class="product-photo" role="img" aria-label="Dog lying in a black round pet bed" style="background:linear-gradient(#f4f4f4,#2e2e2e 60%,#f4f4f4)"></div><p class="product-title">Lorem ipsum dolor sit amet,<br>consectetuer elit</p><p class="product-price">$875.25</p><div class="add-cart">Add to Cart</div></div>
  <div class="product"><div class="product-photo" role="img" aria-label="Dog resting in an olive green pet bed" style="background:linear-gradient(#f4f4f4,#4a5444 60%,#f4f4f4)"></div><p class="product-title">Lorem ipsum dolor sit amet,<br>consectetuer elit</p><p class="product-price">$875.25</p><div class="add-cart">Add to Cart</div></div>
  <div class="product"><div class="product-photo" role="img" aria-label="Dog lounging on an orange cushion bed indoors" style="background:linear-gradient(#c9b8a8,#ec6a2a 60%,#b9a89a)"></div><p class="product-title">Lorem ipsum dolor sit amet,<br>consectetuer elit</p><p class="product-price">$875.25</p><div class="add-cart">Add to Cart</div></div>
  <div class="product"><div class="product-photo" role="img" aria-label="Small dog wearing a green plaid coat" style="background:linear-gradient(90deg,#fff 20%,#4b5a48 50%,#fff 80%)"></div><p class="product-title">Lorem ipsum dolor sit amet,<br>consectetuer elit</p><p class="product-price">$875.25</p><div class="add-cart">Add to Cart</div></div>
  <div class="product"><div class="product-photo" role="img" aria-label="Curly dog in a blue and yellow jacket" style="background:linear-gradient(90deg,#fff 20%,#2f6fb0 45%,#e9c92b 60%,#fff 80%)"></div><p class="product-title">Lorem ipsum dolor sit amet,<br>consectetuer elit</p><p class="product-price">$875.25</p><div class="add-cart">Add to Cart</div></div>
  <div class="product"><div class="product-photo" role="img" aria-label="Dog lying on a grey bolster bed on a wood floor" style="background:linear-gradient(#d8d2c8,#555 55%,#6b4a32)"></div><p class="product-title">Lorem ipsum dolor sit amet,<br>consectetuer elit</p><p class="product-price">$875.25</p><div class="add-cart">Add to Cart</div></div>
</section>

<footer class="footer">
  <div class="footer-col" style="left:89px"><h3>Pages</h3><ul><li>Home</li><li>Blog</li><li>E-commerce</li><li>Reservations</li><li>Event Calendar</li><li>Photos</li><li>Videos</li><li>News</li></ul></div>
  <div class="footer-col" style="left:436px"><h3>Customer Service</h3><ul><li>Contact us</li><li>Shipping Information</li><li>Ordering &amp; Payment</li><li>Returns and Exchanges</li><li>Guaranteed Tough</li><li>Charities Seeking Donations</li><li>Privacy &amp; Email Policies</li></ul></div>
  <div class="footer-col news" style="left:784px"><h3>Latest News</h3>
    <p>Lorem ipsum dolor sit amet, consectetuer adipiscing elit. Aenean commodo ligula</p><time>26th May 2014</time>
    <p>Lorem ipsum dolor sit amet, consectetuer adipiscing elit. Aenean commodo ligula</p><time>26th May 2014</time>
  </div>
</footer>
<div class="copyright">© 2014 MossyDenPetSupply - All Rights Reserved.</div>
</body>
</html>
```